Business Card and Letterhead for Nurlo - modern real estate business

I need a double sided business card design for Nurlo. Please see business card brief here https://papers.trelvimo.net/sheet/q/7XrTbaLeZpMmQ2uWvd9HkCj4yNoEfsGi3lRtAz_pk/view?mode=shared

Please feel free to design the business cards however you feel best. I am happy to give some creative freedoms and then provide feedback from there.

Please then also create a letterhead to match the business card design

Colors

Designer to choose colors to be used in the design.

Requirements
Must have
• Must be a modern, elegant business card which looks very professional

```html
<!DOCTYPE html>
<html lang="en">
<head>
<meta charset="utf-8">
<title>Nurlo Stationery</title>
<link rel="stylesheet" href="https://fonts.googleapis.com/css2?family=Montserrat:wght@400;500;600;700&display=swap">
<style>
:root{
  --red:#e3131b;
  --red-soft:#e9b8bc;
  --ink:#1d1d1d;
  --paper:#efeff1;
  --card-dark:#231f20;
  --backdrop:#7f8284;
  --photo-a:#6b7a6a;
  --photo-b:#2f3a33;
}
*{box-sizing:border-box;margin:0;padding:0}
html,body{width:1200px;height:1019px;overflow:hidden}
body{background:var(--backdrop);font-family:"Montserrat",sans-serif;color:var(--ink);position:relative}

.letterhead{position:absolute;left:206px;top:144px;width:525px;height:700px;background:var(--paper)}
.brand{font-family:"Montserrat",sans-serif;font-weight:600;color:var(--red);letter-spacing:1px;line-height:1}
.letterhead .brand{position:absolute;right:38px;top:34px;font-size:29px}
.name-strip{position:absolute;writing-mode:vertical-rl;transform:rotate(180deg);color:var(--red-soft);font-weight:500;letter-spacing:1px;white-space:nowrap;overflow:hidden}
.letterhead .name-strip{left:503px;top:30px;height:645px;font-size:11px;word-spacing:22px}
.letter-title{position:absolute;left:33px;top:149px;font-size:12px;font-weight:700;letter-spacing:2.4px;color:var(--red)}
.letter-body{position:absolute;left:33px;top:224px;width:456px;font-size:8.3px;line-height:10.6px;text-align:justify}
.letter-body p{margin-bottom:8px}
.letter-address{position:absolute;left:32px;top:600px;font-size:9.5px;letter-spacing:1.8px;line-height:12px}
.letter-contact{position:absolute;left:32px;top:634px;font-size:9.5px;font-weight:700;letter-spacing:1.8px;line-height:12px;color:var(--red)}
.signature{position:absolute;left:360px;top:604px;width:102px;height:30px;background:linear-gradient(90deg,#e4e4e6,#dcdcde)}

.card{position:absolute;left:772px;width:315px;height:177px}
.card-front{top:390px;background:var(--paper)}
.card-back{top:662px;background:var(--card-dark);display:flex;align-items:center;justify-content:center}
.card-back .brand{font-size:50px;letter-spacing:2px}
.portrait{position:absolute;left:27px;top:22px;width:110px;height:110px}
.agent-name{position:absolute;left:0;width:165px;top:143px;text-align:center;font-size:15px;font-weight:500;color:var(--red);letter-spacing:.5px}
.card-front .name-strip{left:164px;top:20px;height:140px;font-size:13px}
.licence-badge{position:absolute;left:196px;top:23px;width:98px;height:22px;background:var(--red);color:#fff;font-size:7px;line-height:8px;letter-spacing:.6px;padding:3px 7px;text-transform:uppercase}
.card-details{position:absolute;left:196px;top:96px;font-size:8.3px;letter-spacing:.9px;line-height:10.5px}
.card-details .web{font-weight:700;margin:7px 0 8px}
.card-details .web span{color:var(--red)}
</style>
</head>
<body>

<section class="letterhead">
  <div class="brand">NURLO</div>
  <div class="name-strip">NURLO NURLO NURLO NURLO NURLO NURLO NURLO NURLO NURLO NURLO</div>
  <h1 class="letter-title">LOREM IPSUM</h1>
  <div class="letter-body">
    <p>Lorem ipsum dolor sit amet, consectetur adipiscing elit, sed do eiusmod tempor incididunt ut labore et dolore magna aliqua. In iaculis nunc sed augue lacus viverra vitae congue. Tempor orci eu lobortis elementum nibh tellus molestie. Nisl pretium fusce id velit ut. Platea dictumst vestibulum rhoncus est pellentesque elit ullamcorper. Laoreet id donec ultrices tincidunt arcu non. Turpis egestas maecenas pharetra convallis posuere morbi. Massa vitae tortor condimentum lacinia. Suspendisse interdum consectetur libero id. Proin fermentum leo vel orci porta non. Sed id semper risus in hendrerit gravida rutrum quisque non. Sagittis vitae et leo duis ut diam quam nulla. Amet justo donec enim diam vulputate ut. Diam donec adipiscing tristique risus nec feugiat in fermentum. Facilisis leo vel fringilla est. Tempor commodo ullamcorper a lacus vestibulum sed arcu non. Magna etiam tempor orci eu lobortis elementum nibh tellus.</p>
    <p>Massa sapien faucibus et molestie ac feugiat sed lectus vestibulum. Pellentesque adipiscing commodo elit at imperdiet dui accumsan sit. Bibendum neque egestas congue quisque egestas diam in arcu cursus. Nisi quis eleifend quam adipiscing vitae proin. Placerat vestibulum lectus mauris ultrices eros in cursus. Dolor sit amet consectetur adipiscing elit duis. Malesuada proin libero nunc consequat interdum varius sit amet mattis. Pretium vulputate sapien nec sagittis aliquam malesuada bibendum arcu. Morbi tristique senectus et netus et malesuada. Malesuada bibendum arcu vitae elementum curabitur vitae nunc. Amet volutpat consequat mauris nunc congue nisi vitae suscipit. Tincidunt ornare massa eget egestas purus viverra accumsan in. Risus in hendrerit gravida rutrum quisque non tellus orci. Fermentum leo vel orci porta.</p>
    <p>Sit amet facilisis magna etiam. Massa enim nec dui nunc mattis enim ut tellus. Ut placerat orci nulla pellentesque dignissim enim sit amet. Duis ut diam quam nulla porttitor massa. Ut porttitor leo a diam sollicitudin tempor. Felis eget velit aliquet sagittis. Fringilla phasellus faucibus scelerisque eleifend donec pretium vulputate sapien nec. Cursus metus aliquam eleifend mi in nulla. Euismod lacinia at quis risus sed vulputate odio ut. Tellus orci ac auctor augue mauris augue neque gravida. Consectetur adipiscing elit duis tristique sollicitudin nibh sit amet. Id donec ultrices tincidunt arcu. Vestibulum sed arcu non odio euismod lacinia. Pharetra et ultrices neque ornare aenean.</p>
  </div>
  <address class="letter-address" style="font-style:normal">PO BOX 3190<br>FERNVALE NSW 2790</address>
  <div class="letter-contact">0412 580 394<br>LIAM@NURLO.COM<br>WWW.NURLO.COM</div>
  <div class="signature" role="img" aria-label="Handwritten signature"></div>
</section>

<section class="card card-front">
  <svg class="portrait" viewBox="0 0 110 110" role="img" aria-label="Portrait photo of the agent">
    <defs>
      <linearGradient id="photoTone" x1="0" y1="0" x2="0" y2="1">
        <stop offset="0" stop-color="var(--photo-a)"/>
        <stop offset="1" stop-color="var(--photo-b)"/>
      </linearGradient>
    </defs>
    <circle cx="55" cy="55" r="52" fill="url(#photoTone)"/>
    <circle cx="55" cy="55" r="53" fill="none" stroke="var(--ink)" stroke-width="3"/>
    <path d="M12 30 A53 53 0 1 1 40 106" fill="none" stroke="var(--red)" stroke-width="3"/>
  </svg>
  <div class="agent-name">LIAM CARVER</div>
  <div class="name-strip">NURLO</div>
  <div class="licence-badge">Licenced real<br>estate agent</div>
  <div class="card-details">
    <div>0412 580 394<br>LIAM@NURLO.COM</div>
    <div class="web">WWW.<span>NURLO</span>.COM</div>
    <div>PO BOX 3190<br>FERNVALE NSW 2790</div>
  </div>
</section>

<section class="card card-back">
  <div class="brand">NURLO</div>
</section>

</body>
</html>
```